Oil and Gas Exploration and Production company needs a business card design

We need a business card design using our logo and colors in the logo. We want a mainstream design.

```html
<!DOCTYPE html>
<html lang="en">
<head>
<meta charset="utf-8">
<title>Solvane Oil &amp; Gas — Business Card</title>
<link rel="stylesheet" href="https://fonts.googleapis.com/css2?family=Open+Sans:wght@400;700&display=swap">
<style>
  :root {
    --bg: #e6e6e4;
    --card: #ffffff;
    --ink: #141414;
    --gold: #d8a22a;
    --muted: #555555;
    --rule: #dcdcdc;
  }
  * { box-sizing: border-box; margin: 0; padding: 0; }
  html, body { width: 1200px; height: 900px; overflow: hidden; }
  body {
    background: var(--bg);
    font-family: "Open Sans", Arial, sans-serif;
    color: var(--ink);
    position: relative;
  }
  .card {
    position: absolute;
    width: 540px;
    height: 310px;
    background: var(--card);
    border-radius: 18px;
    box-shadow: 0 6px 18px rgba(0,0,0,0.12);
  }
  .card-front { left: 70px; top: 130px; }
  .card-back  { left: 590px; top: 460px; }

  .brand {
    display: flex;
    align-items: center;
    gap: 12px;
  }
  .brand-dot {
    width: 26px; height: 26px;
    border-radius: 50%;
    background: var(--gold);
    flex: none;
  }
  .brand-name {
    font-weight: 700;
    font-size: 34px;
    letter-spacing: -0.5px;
    color: var(--ink);
    white-space: nowrap;
  }

  .card-front .brand {
    position: absolute;
    left: 0; right: 0; top: 112px;
    justify-content: center;
  }
  .front-web {
    position: absolute;
    left: 0; right: 0; top: 214px;
    text-align: center;
    font-size: 13px;
    letter-spacing: 6px;
    color: var(--muted);
  }

  .card-back .brand {
    position: absolute;
    left: 28px; top: 135px;
  }
  .card-back .brand-name { font-size: 27px; }
  .card-back .brand-dot { width: 22px; height: 22px; }

  .divider {
    position: absolute;
    left: 300px; top: 40px; bottom: 40px;
    width: 1px;
    background: var(--rule);
  }
  .contact {
    position: absolute;
    left: 322px; top: 66px;
    font-size: 12.5px;
    line-height: 1.45;
    color: #333;
  }
  .person-name {
    font-weight: 700;
    font-size: 15px;
    color: var(--ink);
    letter-spacing: 0.3px;
  }
  .person-title {
    color: var(--gold);
    font-size: 12.5px;
    margin-bottom: 6px;
  }
  .address { margin-bottom: 4px; }
  .contact-list { list-style: none; }
  .contact-list li {
    display: flex;
    align-items: center;
    gap: 8px;
  }
  .contact-list svg { width: 11px; height: 11px; flex: none; fill: var(--ink); }
</style>
</head>
<body>

  <section class="card card-front">
    <div class="brand">
      <span class="brand-dot"></span>
      <span class="brand-name">Solvane Oil &amp; Gas</span>
    </div>
    <p class="front-web">www.solvaneoil.com</p>
  </section>

  <section class="card card-back">
    <div class="brand">
      <span class="brand-dot"></span>
      <span class="brand-name">Solvane Oil &amp; Gas</span>
    </div>
    <div class="divider"></div>
    <div class="contact">
      <p class="person-name">MARK HALDEN</p>
      <p class="person-title">PRESIDENT</p>
      <p class="address">2170 Carver Lane<br>Millbrook, NY 12545</p>
      <ul class="contact-list">
        <li>
          <svg viewBox="0 0 12 12" aria-hidden="true"><path d="M2.5 1 4.5 1 5.3 3.4 4 4.4C4.6 5.8 6.2 7.4 7.6 8L8.6 6.7 11 7.5 11 9.5C11 10.3 10.3 11 9.5 11 5 11 1 7 1 2.5 1 1.7 1.7 1 2.5 1Z"/></svg>
          555 0142 2253
        </li>
        <li>
          <svg viewBox="0 0 12 12" aria-hidden="true"><path d="M3.5 0.5h5a1 1 0 0 1 1 1v9a1 1 0 0 1-1 1h-5a1 1 0 0 1-1-1v-9a1 1 0 0 1 1-1Zm0.5 1.5v7h4V2Z"/></svg>
          555 0187 5335
        </li>
        <li>
          <svg viewBox="0 0 12 12" aria-hidden="true"><path d="M3 1h6v3H3Zm-2 4h10v5H9v2H3v-2H1Zm3 3v3h4V8Z"/></svg>
          555 0163 3856
        </li>
        <li>
          <svg viewBox="0 0 12 12" aria-hidden="true"><path d="M1 2.5h10v7H1Zm1 1v.4l4 2.6 4-2.6v-.4Z"/></svg>
          info@solvaneoil.com
        </li>
        <li>
          <svg viewBox="0 0 12 12" aria-hidden="true"><circle cx="6" cy="6" r="5"/></svg>
          www.solvaneoil.com
        </li>
      </ul>
    </div>
  </section>

</body>
</html>
```